Logo redesign & Stationery Design Project

We need a logo redesign for our company.

We also require the following stationary with the new logo:
*letterhead
*With compliments slips
*business card
*envelopes

We would like to maintain our current colours of navy blue and gold. We would like to maintain the wording on the back of our current business card.

Our existing letterhead and business card is attached.

Target Market(s)

Medical Professionals, Pharmacists, Lawyers

Industry/Entity Type

Business

Requirements
Must have
• See attached business card and letterhead, as all details on these documents need to be included.

```html
<!DOCTYPE html>
<html lang="en">
<head>
<meta charset="utf-8">
<title>Halden Marsh Financial Services – Stationery</title>
<link href="https://fonts.googleapis.com/css2?family=Montserrat:wght@300;400;500;600&family=Great+Vibes&display=swap" rel="stylesheet">
<style>
:root{
  --navy:#1f3461;
  --gold:#a58a54;
  --paper:#f5f5f6;
  --ink:#4a4f5c;
  --muted:#8a8f99;
  --backdrop:#e6e7ea;
}
*{box-sizing:border-box;margin:0;padding:0}
html,body{width:1200px;height:754px;overflow:hidden;background:var(--backdrop);font-family:"Montserrat",sans-serif;color:var(--ink)}
.canvas{position:relative;width:1200px;height:754px}
.sheet{position:absolute;background:var(--paper);box-shadow:0 4px 14px rgba(0,0,0,.12)}

/* brand lockup */
.brand{display:flex;align-items:center;gap:8px}
.brand-dot{border:2px solid var(--navy);border-radius:50%;flex:none}
.brand-name{font-weight:500;color:var(--navy);line-height:1}
.brand-sub{font-weight:400;color:var(--muted);line-height:1.2;margin-top:2px}

/* envelope */
.envelope{left:30px;top:270px;width:310px;height:155px;border-bottom:9px solid var(--navy)}
.envelope .brand{position:absolute;left:16px;top:16px}
.envelope .brand-dot{width:24px;height:24px}
.envelope .brand-name{font-size:11px}
.envelope .brand-sub{font-size:6px}
.envelope .address{position:absolute;left:16px;top:50px;font-size:5px;line-height:1.5;color:var(--muted)}

/* letterhead */
.letterhead{left:370px;top:30px;width:480px;height:690px}
.letterhead .brand{position:absolute;left:38px;top:40px}
.letterhead .brand-dot{width:34px;height:34px}
.letterhead .brand-name{font-size:16px}
.letterhead .brand-sub{font-size:8px}
.letterhead .contact{position:absolute;right:38px;top:36px;font-size:6px;line-height:1.55;color:var(--muted);text-align:left}
.letter{position:absolute;left:60px;right:50px;top:150px;font-size:7.2px;line-height:1.6;color:var(--ink)}
.letter .salutation{font-weight:600;margin-bottom:10px}
.letter p{margin-bottom:10px}
.signature{position:absolute;left:60px;top:520px}
.signature .script{font-family:"Great Vibes",cursive;font-size:28px;color:var(--ink);line-height:1}
.signature .role{font-size:7.5px;font-weight:600;color:var(--ink);margin-top:2px}
.footer-band{position:absolute;left:0;right:0;bottom:22px;height:22px;background:var(--navy);color:#fff;font-size:7.5px;font-weight:300;display:flex;align-items:center;justify-content:center;letter-spacing:.02em}

/* business cards */
.card{width:270px;height:150px}
.card-front{left:895px;top:140px;border-left:4px solid var(--navy);border-bottom:4px solid var(--navy)}
.card-front .person{position:absolute;left:16px;top:16px}
.card-front .person-name{font-size:10px;font-weight:500;color:var(--navy)}
.card-front .person-title{font-size:7px;color:var(--muted);margin-top:2px}
.card-front .contact-list{position:absolute;left:16px;top:52px;list-style:none;font-size:6px;line-height:1.7;color:var(--muted)}
.card-front .contact-list li{display:flex;align-items:center;gap:5px}
.card-front .contact-list svg{width:7px;height:7px;fill:var(--navy)}
.card-front .brand{position:absolute;right:16px;bottom:18px}
.card-front .brand-dot{width:22px;height:22px}
.card-front .brand-name{font-size:11px}
.card-front .brand-sub{font-size:6px}

.card-back{left:895px;top:330px;background:var(--navy);color:#fff;padding:14px 18px}
.card-back .brand-dot{width:12px;height:12px;border-color:#fff}
.card-back .brand-name{font-size:8px;color:#fff}
.card-back .values{margin-top:8px}
.card-back .value{font-size:15px;font-weight:300;letter-spacing:.08em;line-height:1}
.card-back .value-line{font-size:4.6px;letter-spacing:.12em;color:#c8cde0;margin:2px 0 4px}
.card-back .rule{height:1px;background:var(--gold);margin:4px 0 5px}
.card-back .web{font-size:6px;letter-spacing:.04em}
.card-back .legal{font-size:4.6px;color:#c8cde0;margin-top:2px}
</style>
</head>
<body>
<div class="canvas">

  <section class="sheet envelope" aria-label="DL envelope">
    <div class="brand">
      <span class="brand-dot"></span>
      <div><div class="brand-name">Halden Marsh</div><div class="brand-sub">Financial Services</div></div>
    </div>
    <div class="address">Suite 4, 112-118 Harbour Road Lindenvale NSW 2290<br>PO Box 4417 Lindenvale NSW 2290<br>www.haldenmarsh.com.au</div>
  </section>

  <section class="sheet letterhead" aria-label="Letterhead">
    <div class="brand">
      <span class="brand-dot"></span>
      <div><div class="brand-name">Halden Marsh</div><div class="brand-sub">Financial Services</div></div>
    </div>
    <div class="contact">
      Suite 4, 112-118 Harbour Road Lindenvale NSW 2290<br>
      PO Box 4417 Lindenvale NSW 2290<br>
      T 02 9481 2205 &nbsp;F 02 9481 2206<br>
      E info@haldenmarsh.com.au<br>
      www.haldenmarsh.com.au<br>
      ABN 52 180 417 663
    </div>
    <div class="letter">
      <div class="salutation">Lorem Ipsum,</div>
      <p>Cras mattis consectetur purus sit amet fermentum. Etiam porta sem malesuada magna mollis euismod. Integer posuere erat a ante venenatis dapibus posuere velit aliquet. Cras justo odio, dapibus ac facilisis in, egestas eget quam. Aenean eu leo quam. Pellentesque ornare sem lacinia quam venenatis vestibulum.</p>
      <p>Vivamus sagittis lacus vel augue laoreet rutrum faucibus dolor auctor. Donec sed odio dui. Etiam porta sem malesuada magna mollis euismod. Morbi leo risus, porta ac consectetur ac, vestibulum at eros. Nullam id dolor id nibh ultricies vehicula ut id elit.</p>
      <p>Donec id elit non mi porta gravida at eget metus. Fusce dapibus, tellus ac cursus commodo, tortor mauris condimentum nibh, ut fermentum massa justo sit amet risus. Cras justo odio, dapibus ac facilisis in, egestas eget quam. Cum sociis natoque penatibus et magnis dis parturient montes, nascetur ridiculus mus.</p>
      <p>Cum sociis natoque penatibus et magnis dis parturient montes, nascetur ridiculus mus. Curabitur blandit tempus porttitor. Aenean lacinia bibendum nulla sed consectetur. Lorem ipsum dolor sit amet, consectetur adipiscing elit.</p>
      <p>Cras justo odio, dapibus ac facilisis in, egestas eget quam. Morbi leo risus, porta ac consectetur ac, vestibulum at eros. Duis mollis, est non commodo luctus, nisi erat porttitor ligula, eget lacinia odio sem nec elit. Integer posuere erat a ante venenatis dapibus posuere velit aliquet. Vivamus sagittis lacus vel augue laoreet rutrum faucibus dolor auctor.</p>
    </div>
    <div class="signature">
      <div class="script">Your Name</div>
      <div class="role">Company Director</div>
    </div>
    <div class="footer-band">Corporate Authorised Representative of Northgate Advisory Partners AFSL 418205</div>
  </section>

  <section class="sheet card card-front" aria-label="Business card front">
    <div class="person">
      <div class="person-name">Elias (Eli) HALDEN</div>
      <div class="person-title">Partner</div>
    </div>
    <ul class="contact-list">
      <li><svg viewBox="0 0 10 10"><path d="M2 1h2l1 2.5-1.2.8a6 6 0 0 0 2 2l.8-1.2L9 6v2a1 1 0 0 1-1 1A7 7 0 0 1 1 2a1 1 0 0 1 1-1z"/></svg>Suite 4, 112-118 Harbour Road Lindenvale</li>
      <li><svg viewBox="0 0 10 10"><path d="M2 1h2l1 2.5-1.2.8a6 6 0 0 0 2 2l.8-1.2L9 6v2a1 1 0 0 1-1 1A7 7 0 0 1 1 2a1 1 0 0 1 1-1z"/></svg>02 9481 2205</li>
      <li><svg viewBox="0 0 10 10"><path d="M2 1h2l1 2.5-1.2.8a6 6 0 0 0 2 2l.8-1.2L9 6v2a1 1 0 0 1-1 1A7 7 0 0 1 1 2a1 1 0 0 1 1-1z"/></svg>0412 608 374</li>
      <li><svg viewBox="0 0 10 10"><path d="M1 2h8v6H1zM1 2l4 3.5L9 2" fill="none" stroke="#1f3461"/></svg>eli@haldenmarsh.com.au</li>
    </ul>
    <div class="brand">
      <span class="brand-dot"></span>
      <div><div class="brand-name">Halden Marsh</div><div class="brand-sub">Financial Services</div></div>
    </div>
  </section>

  <section class="sheet card card-back" aria-label="Business card back">
    <div class="brand">
      <span class="brand-dot"></span>
      <div class="brand-name">Halden Marsh</div>
    </div>
    <div class="values">
      <div class="value">CERTAINTY</div>
      <div class="value-line">DESIGNING INSURANCE SOLUTIONS</div>
      <div class="value">CLARITY</div>
      <div class="value-line">STRATEGIC PLANNING ADVICE</div>
      <div class="value">CONFIDENCE</div>
      <div class="value-line">CONSTRUCTING RETIREMENT PLANS</div>
    </div>
    <div class="rule"></div>
    <div class="web">www.haldenmarsh.com.au</div>
    <div class="legal">Corporate Authorised Representative of Northgate Advisory Partners AFSL 418205</div>
  </section>

</div>
</body>
</html>
```